Invitation Design for TORAM KELPANE Investigator Event (Exclusive Cocktail Reception)

Project Overview:
Toram Cellworks is hosting an exclusive, invitation-only cocktail reception for KELPANE clinical study investigators during the ODRIM 2026 Conference. We need a polished, high-end event invitation designed for both email and print formats.
Event Details:
Event Name: Gather & Grow: The KELPANE Investigator Event
Date: Saturday, January 24
Time: 5:00–7:00 PM
Location: Walter Brisk Chophouse (Hartwell Private Room), Orlean Terrace
Purpose: A relaxed, come-and-go cocktail reception for KELPANE investigators to mingle; light content and conversation, no formal presentations.
Design Requirements:
Two logos required:
TORAM (primary)
KELPANE (secondary)
Color Palette: Use the Toram color scheme, KELPANE color scheme, or a clean blend of both.
Tone & Style: Premium, modern, medical-professional with a high-end reception feel
Deliverable Layout:
Event title
Date & time
Location
Blurb: You are invited to a gathering for KELPANE clinical investigators. This event is intended to provide an opportunity for professional discussion, study related updates, and peer connection within the investigator community.
Both required logos
Clean, elegant spacing with strong hierarchy
What We Want
A visually striking but clean design that feels:
Sophisticated and corporate-professional
Consistent with our brand aesthetic
Appropriate for a high-profile physician audience
Think: elevated, clinical, modern — not flashy or overly busy.
Audience
Physicians and researchers participating in the KELPANE clinical study — a high-end, professional group.

```html
<!DOCTYPE html>
<html lang="en">
<head>
<meta charset="utf-8">
<title>Gather &amp; Grow: The KELPANE Investigator Event</title>
<link href="https://fonts.googleapis.com/css2?family=Source+Serif+4:opsz,wght@8..60,400;8..60,700&display=swap" rel="stylesheet">
<style>
  :root {
    --canvas-grey: #bdbec0;
    --card-white: #f2f2f1;
    --accent-orange: #d9773a;
    --ink-navy: #1c2a52;
    --text-navy: #2b3658;
    --brand-green: #7cc043;
    --divider-grey: #a9a9a9;
  }
  * { margin: 0; padding: 0; box-sizing: border-box; }
  html, body { width: 1200px; height: 1200px; overflow: hidden; }
  body {
    background: var(--canvas-grey);
    font-family: "Source Serif 4", Georgia, serif;
    position: relative;
  }
  .invitation {
    position: absolute;
    left: 0; top: 312px;
    width: 1200px; height: 576px;
    background: var(--card-white);
  }
  .line {
    position: absolute;
    left: 0; width: 100%;
    text-align: center;
    color: var(--ink-navy);
    line-height: 1;
  }
  .event-title {
    top: 68px;
    font-size: 64px;
    font-weight: 700;
    color: var(--accent-orange);
    letter-spacing: 0.5px;
  }
  .event-subtitle {
    top: 145px;
    font-size: 36px;
    font-weight: 700;
  }
  .event-detail {
    font-size: 23px;
    font-weight: 700;
  }
  .event-date { top: 218px; }
  .event-time { top: 245px; }
  .event-venue { top: 272px; }
  .event-venue .venue-room { font-weight: 400; }
  .event-city { top: 298px; }
  .event-blurb {
    position: absolute;
    left: 300px; top: 338px;
    width: 600px;
    text-align: center;
    font-size: 16px;
    line-height: 21px;
    color: var(--text-navy);
  }
  .brand-row {
    position: absolute;
    left: 0; top: 444px;
    width: 100%; height: 80px;
  }
  .brand-primary {
    position: absolute;
    left: 350px; top: 8px;
    font-size: 60px;
    font-weight: 400;
    color: var(--brand-green);
    letter-spacing: 2px;
    line-height: 1;
  }
  .brand-divider {
    position: absolute;
    left: 580px; top: 0;
    width: 2px; height: 80px;
    background: var(--divider-grey);
  }
  .brand-secondary {
    position: absolute;
    left: 614px; top: 18px;
    display: flex; align-items: center; gap: 8px;
  }
  .brand-secondary .brand-square {
    width: 22px; height: 22px;
    background: var(--ink-navy);
  }
  .brand-secondary .brand-name {
    font-size: 32px;
    font-weight: 700;
    color: var(--ink-navy);
    line-height: 1;
  }
</style>
</head>
<body>
  <main class="invitation">
    <h1 class="line event-title">Gather &amp; Grow:</h1>
    <h2 class="line event-subtitle">The KELPANE Investigator Event</h2>

    <p class="line event-detail event-date">Saturday, January 24</p>
    <p class="line event-detail event-time">5:00 – 7:00 PM</p>
    <p class="line event-detail event-venue">Walter Brisk Chophouse <span class="venue-room">(Hartwell Private Room),</span></p>
    <p class="line event-detail event-city">Orlean Terrace</p>

    <p class="event-blurb">You are invited to a gathering for KELPANE clinical investigators. This event is intended to provide an opportunity for professional discussion, study related updates, and peer connection within the investigator community.</p>

    <div class="brand-row">
      <div class="brand-primary">TORAM</div>
      <div class="brand-divider"></div>
      <div class="brand-secondary">
        <span class="brand-square"></span>
        <span class="brand-name">KELPANE U.S.</span>
      </div>
    </div>
  </main>
</body>
</html>
```